Box Packaging Design for Desktop Zen Garden

We need a box packing design for a small family-owned company.
We create a desktop zen garden for office display. We would like you to create a clean box package design so that a potential customer would like to grab our product on the shelf.

1. We would like to name this desktop zen garden kit "pelumi" (please find a suitable font that would match the zen garden display )
2. Size of the zen garden kit (wooden tray): 25cm*25cm*1cm
3. Size of the box: 30.4cm*30.4cm*4.5cm
4. Barcode on the back (attached)
5. The box package must have Made in China on the back
6. We don't have professional photos taken yet. Once we have your box design, we will prepare the professional photo to replace image so don't spend much time editing the attached photo.

Target Market(s)

Office space, Home decor, Spa, Gift

Industry/Entity Type

Home And Garden

Colors

Designer to choose colors to be used in the design.

Requirements
Must have
• 1. The brand is TORVEL (logo attached. The font is ALEWISDODI)
• 2. The box packaging must convey the benefit of using this desktop zen garden.

```html
<!DOCTYPE html>
<html lang="en">
<head>
<meta charset="utf-8">
<title>pelumi – desktop zen garden box</title>
<link rel="stylesheet" href="https://fonts.googleapis.com/css2?family=Lato:wght@300;400&display=swap">
<style>
  :root {
    --page: #ffffff;
    --sand-light: #f2eee8;
    --sand-mid: #ddd5ca;
    --sand-deep: #bfb4a5;
    --sand-shadow: #a89c8c;
    --side-panel: #f7f6f4;
    --ink: #3b3733;
    --ink-soft: #55504a;
  }
  * { margin: 0; padding: 0; box-sizing: border-box; }
  html, body {
    width: 807px;
    height: 1200px;
    overflow: hidden;
    background: var(--page);
  }
  .canvas {
    position: relative;
    width: 807px;
    height: 1200px;
    background: var(--page);
    font-family: "Lato", sans-serif;
  }

  /* Box lid, front face */
  .box-front {
    position: absolute;
    left: 38px;
    top: 34px;
    width: 732px;
    height: 690px;
    overflow: hidden;
  }
  .sand-photo {
    position: absolute;
    inset: 0;
    background:
      radial-gradient(ellipse 40% 55% at 72% 30%, var(--sand-shadow) 0%, transparent 70%),
      radial-gradient(ellipse 35% 45% at 62% 82%, var(--sand-deep) 0%, transparent 70%),
      radial-gradient(ellipse 30% 50% at 92% 60%, var(--sand-light) 0%, transparent 70%),
      linear-gradient(170deg, var(--sand-light) 0%, var(--sand-mid) 55%, var(--sand-deep) 100%);
  }
  .brand-block {
    position: absolute;
    left: 36px;
    top: 462px;
    color: var(--ink);
  }
  .product-name {
    font-weight: 300;
    font-size: 56px;
    line-height: 1;
    letter-spacing: 0.5px;
  }
  .product-tagline {
    margin-top: 6px;
    font-weight: 300;
    font-size: 21px;
    letter-spacing: 0.3px;
    color: var(--ink-soft);
  }

  /* Box side band */
  .box-side {
    position: absolute;
    left: 38px;
    top: 770px;
    width: 732px;
    height: 108px;
    background: var(--side-panel);
    border: 1px solid #e6e2dc;
    display: flex;
    align-items: center;
    justify-content: flex-end;
    padding-right: 70px;
  }
  .side-label {
    font-weight: 300;
    font-size: 24px;
    color: var(--ink);
    letter-spacing: 0.3px;
  }
</style>
</head>
<body>
  <main class="canvas">
    <section class="box-front">
      <div class="sand-photo" role="img" aria-label="Photograph of raked sand with flowing wave ripples in a zen garden"></div>
      <div class="brand-block">
        <h1 class="product-name">pelumi</h1>
        <p class="product-tagline">desktop zen garden</p>
      </div>
    </section>
    <section class="box-side">
      <p class="side-label">pelumi desktop zen garden</p>
    </section>
  </main>
</body>
</html>
```